Pemberly property maintenance house wash and water tank cleaning trailer

Pemberly property maintenance is an exterior cleaning company, we have built a new trailer for cleaning water tanks and buildings. We would like a design that incorporates our company name, logo, phone number and web page. The trailer has 11 aluminum panels on it as you will see in the pics, we would like a design that brings it all together. The front 2 corner panels get a bit dirty, so our thought were we might be able to have a design that makes the front of the trailer look dirty and the rest look clean. For example a mud splash in the background on the front panels and maybe the front side panels and then the rest of the panels looking like they are soaped up or clean. www.pemberlypropertymaintenance.co.nz for details

Requirements
Must have
• A design that is eye catching
Nice to have
• some use of our company colors ( see pics or website ) www.pemberlypropertymaintnenance.co.nz

Website across the rear of the trailer
Should not have
• plain design

```html
<!DOCTYPE html>
<html lang="en">
<head>
<meta charset="utf-8">
<title>Pemberly Property Maintenance – Trailer Panels</title>
<link rel="stylesheet" href="https://fonts.googleapis.com/css2?family=Stardos+Stencil:wght@700&family=Inconsolata:wght@500&family=Roboto:wght@400;700&display=swap">
<style>
  :root {
    --brand-red: #ed1c24;
    --brand-deep-red: #d4111a;
    --brand-yellow: #fff200;
    --ink: #231f20;
    --paper: #ffffff;
    --frame-grey: #8a8a8a;
    --tank-blue: #1e8fd8;
    --tank-blue-dark: #0b5fa5;
    --mud: #7a4a22;
  }
  html, body { margin: 0; padding: 0; width: 1200px; height: 801px; overflow: hidden; background: var(--paper); }
  .layout-sheet { display: block; width: 1200px; height: 801px; }
  .panel-red { fill: var(--brand-red); }
  .panel-deep-red { fill: var(--brand-deep-red); }
  .panel-yellow { fill: var(--brand-yellow); }
  .icon-tile { fill: var(--ink); }
  .side-frame { stroke: var(--frame-grey); stroke-width: 1.5; fill: none; }
  .stencil { font-family: "Stardos Stencil", Georgia, serif; font-weight: 700; }
  .stencil-light { fill: var(--paper); }
  .stencil-dark { fill: var(--ink); }
  .stencil-yellow { fill: var(--brand-yellow); }
  .web-address { font-family: "Inconsolata", monospace; font-weight: 500; fill: var(--ink); }
  .sans { font-family: "Roboto", Arial, sans-serif; }
  .tagline-dark { fill: var(--ink); font-weight: 700; }
  .tagline-light { fill: var(--paper); }
  .service-list { fill: var(--paper); }
  .social-name { font-family: "Roboto", Arial, sans-serif; font-weight: 700; fill: var(--paper); }
  .dimension { font-family: "Roboto", Arial, sans-serif; font-size: 11.5px; fill: var(--ink); }
</style>
</head>
<body>
<svg class="layout-sheet" viewBox="0 0 1200 801" xmlns="http://www.w3.org/2000/svg">
  <defs>
    <linearGradient id="tank-fill" x1="0" x2="1" y1="0" y2="0">
      <stop offset="0" stop-color="var(--tank-blue-dark)"/>
      <stop offset="0.5" stop-color="var(--tank-blue)"/>
      <stop offset="1" stop-color="var(--tank-blue-dark)"/>
    </linearGradient>
    <radialGradient id="mud-fill" cx="0.45" cy="0.8" r="0.7">
      <stop offset="0" stop-color="var(--mud)" stop-opacity="0.9"/>
      <stop offset="1" stop-color="var(--mud)" stop-opacity="0"/>
    </radialGradient>
  </defs>

  <!-- Rear panels -->
  <g class="rear-panels">
    <rect class="panel-red" x="64" y="52" width="162" height="87"/>
    <rect class="panel-red" x="271" y="52" width="691" height="87"/>
    <text class="stencil stencil-light" x="620" y="100" font-size="34" text-anchor="middle" textLength="651" lengthAdjust="spacingAndGlyphs">PEMBERLY PROPERTY MAINTENANCE</text>
    <text class="web-address" x="620" y="125" font-size="24" text-anchor="middle" textLength="560" lengthAdjust="spacingAndGlyphs">www.pemberlypropertymaintenance.co.nz</text>
    <rect class="panel-red" x="1000" y="52" width="162" height="87"/>
    <circle cx="1020" cy="84" r="5" fill="var(--paper)"/>
    <text class="social-name" x="1030" y="88" font-size="12">Friendbook</text>
    <circle cx="1020" cy="108" r="5" fill="var(--paper)"/>
    <text class="social-name" x="1030" y="112" font-size="12">Chirpline</text>
    <text class="dimension" x="615" y="41" text-anchor="middle">2325 mm</text>
    <text class="dimension" x="1092" y="152" text-anchor="middle">550 mm</text>
    <text class="dimension" transform="translate(1182 90) rotate(-90)" text-anchor="middle">295 mm</text>
  </g>

  <!-- Side panel, left upper -->
  <g class="side-upper-left">
    <polygon class="panel-red" points="204,189 590,189 504,276 204,276"/>
    <rect class="icon-tile" x="298" y="199" width="38" height="37" role="img" aria-label="Shovel icon"/>
    <rect class="icon-tile" x="342" y="199" width="38" height="37" role="img" aria-label="Loppers icon"/>
    <rect class="icon-tile" x="386" y="199" width="37" height="37" role="img" aria-label="Pressure washer wand icon"/>
    <text class="stencil stencil-light" x="361" y="271" font-size="42" text-anchor="middle" textLength="241" lengthAdjust="spacingAndGlyphs">PEMBERLY</text>
    <text class="dimension" x="318" y="178" text-anchor="middle">1305 mm</text>
    <text class="dimension" x="322" y="293" text-anchor="middle">1037 mm</text>
    <text class="dimension" transform="translate(194 218) rotate(-90)" text-anchor="middle">270 mm</text>
  </g>

  <!-- Side panel, right upper -->
  <g class="side-upper-right">
    <polygon class="panel-red" points="643,192 1028,192 1028,246 696,246"/>
    <polygon class="panel-yellow" points="696,246 1029,246 1029,279 728,279"/>
    <text class="stencil stencil-light" x="871" y="236" font-size="25" text-anchor="middle" textLength="282" lengthAdjust="spacingAndGlyphs">PROPERTY MAINTENANCE</text>
    <text class="sans tagline-dark" x="872" y="268" font-size="19" text-anchor="middle" textLength="284" lengthAdjust="spacingAndGlyphs">Your Exterior Property Specialists</text>
  </g>

  <!-- Side panel, left lower -->
  <g class="side-lower-left">
    <polygon class="panel-red" points="204,312 590,312 504,400 204,400"/>
    <rect class="icon-tile" x="245" y="324" width="63" height="63" role="img" aria-label="Shovel icon"/>
    <rect class="icon-tile" x="319" y="324" width="64" height="63" role="img" aria-label="Loppers icon"/>
    <rect class="icon-tile" x="393" y="324" width="64" height="63" role="img" aria-label="Pressure washer wand icon"/>
    <text class="dimension" transform="translate(194 341) rotate(-90)" text-anchor="middle">270 mm</text>
    <text class="dimension" x="318" y="422" text-anchor="middle">1305 mm</text>
  </g>

  <!-- Side panel, right lower -->
  <g class="side-lower-right">
    <polygon class="panel-red" points="640,315 1025,315 1025,366 689,366"/>
    <polygon class="panel-yellow" points="689,366 1026,366 1026,403 725,403"/>
    <text class="stencil stencil-light" x="868" y="358" font-size="42" text-anchor="middle" textLength="230" lengthAdjust="spacingAndGlyphs">PEMBERLY</text>
    <text class="stencil stencil-dark" x="869" y="393" font-size="24" text-anchor="middle" textLength="284" lengthAdjust="spacingAndGlyphs">PROPERTY MAINTENANCE</text>
  </g>

  <!-- Fender strips and phone panel -->
  <g class="fender-strips">
    <rect class="panel-yellow" x="227" y="447" width="158" height="21"/>
    <text class="dimension" transform="translate(223 459) rotate(-90)" text-anchor="middle" font-size="9">65 mm</text>
    <text class="dimension" x="302" y="482" text-anchor="middle">490 mm</text>
    <rect class="panel-yellow" x="462" y="433" width="304" height="48"/>
    <g class="phone-icon">
      <circle cx="488" cy="457" r="14" fill="none" stroke="var(--ink)" stroke-width="2.5"/>
      <path d="M482 449 q-2 8 5 15 q7 6 11 3 l-3 -4 q-2 1 -4 -1 q-4 -4 -4 -6 q1 -2 1 -3 z" fill="var(--ink)"/>
    </g>
    <text class="stencil stencil-dark" x="635" y="472" font-size="42" text-anchor="middle" textLength="244" lengthAdjust="spacingAndGlyphs">21 555 0148</text>
    <text class="dimension" x="627" y="423" text-anchor="middle">1030 mm</text>
    <text class="dimension" transform="translate(782 456) rotate(-90)" text-anchor="middle">160 mm</text>
    <rect class="panel-yellow" x="837" y="446" width="158" height="20"/>
  </g>

  <!-- Front panel, water tank -->
  <g class="front-left-panel">
    <rect class="panel-deep-red" x="44" y="512" width="201" height="10"/>
    <polygon class="panel-red" points="44,553 245,553 245,676 44,714"/>
    <rect class="panel-yellow" x="44" y="521" width="201" height="32"/>
    <path class="panel-yellow" d="M44 714 Q140 700 245 676 L245 772 L44 764 Z"/>
    <text class="stencil stencil-dark" x="58" y="535" font-size="14.5" textLength="93" lengthAdjust="spacingAndGlyphs">WATER TANK</text>
    <text class="stencil stencil-dark" x="58" y="550" font-size="14.5" textLength="70" lengthAdjust="spacingAndGlyphs">CLEANING</text>
    <circle cx="59" cy="564" r="1.8" fill="var(--paper)"/>
    <text class="sans tagline-light" x="67" y="568" font-size="9.5">Water Tank Clean</text>
    <circle cx="59" cy="581" r="1.8" fill="var(--paper)"/>
    <text class="sans tagline-light" x="67" y="585" font-size="9.5">Water Tank Clean &amp; Sanitize</text>
    <rect x="85" y="607" width="125" height="155" rx="10" fill="url(#tank-fill)" role="img" aria-label="Blue plastic water tank"/>
    <text class="dimension" x="154" y="508" text-anchor="middle">682 mm</text>
    <text class="dimension" transform="translate(40 644) rotate(-90)" text-anchor="middle">880 mm</text>
    <text class="dimension" transform="translate(257 644) rotate(-90)" text-anchor="middle">850 mm</text>
  </g>

  <!-- Front corner, left -->
  <g class="front-corner-left">
    <polygon class="panel-red" points="356,508 420,686 356,673"/>
    <polygon class="panel-yellow" points="356,673 420,688 421,759 356,759"/>
    <polygon class="side-frame" points="356,508 420,686 421,759 356,759"/>
    <text class="dimension" transform="translate(407 592) rotate(-110)" text-anchor="middle">580 mm</text>
    <text class="dimension" transform="translate(351 645) rotate(-90)" text-anchor="middle">840 mm</text>
    <text class="dimension" transform="translate(436 723) rotate(-90)" text-anchor="middle">260 mm</text>
    <text class="dimension" x="390" y="775" text-anchor="middle">210 mm</text>
  </g>

  <!-- Front centre panels -->
  <g class="front-centre">
    <rect class="panel-red" x="470" y="508" width="237" height="169"/>
    <rect class="icon-tile" x="511" y="525" width="46" height="45" role="img" aria-label="Shovel icon"/>
    <rect class="icon-tile" x="564" y="525" width="45" height="45" role="img" aria-label="Loppers icon"/>
    <rect class="icon-tile" x="618" y="525" width="45" height="45" role="img" aria-label="Pressure washer wand icon"/>
    <text class="stencil stencil-light" x="587" y="612" font-size="36" text-anchor="middle" textLength="199" lengthAdjust="spacingAndGlyphs">PEMBERLY</text>
    <rect class="panel-yellow" x="470" y="621" width="237" height="23"/>
    <text class="stencil stencil-dark" x="587" y="638" font-size="17" text-anchor="middle" textLength="196" lengthAdjust="spacingAndGlyphs">PROPERTY MAINTENANCE</text>
    <text class="sans tagline-light" x="588" y="664" font-size="12" text-anchor="middle" textLength="180" lengthAdjust="spacingAndGlyphs">Your Exterior Property Specialists</text>
    <rect class="panel-red" x="470" y="681" width="237" height="74"/>
    <g class="phone-icon-small">
      <circle cx="504" cy="717" r="9.5" fill="none" stroke="var(--brand-yellow)" stroke-width="2"/>
      <path d="M500 712 q-1 5 3 9 q4 4 7 2 l-2 -3 q-1 1 -3 -1 q-2 -2 -2 -4 q1 -1 1 -2 z" fill="var(--brand-yellow)"/>
    </g>
    <text class="stencil stencil-yellow" x="596" y="727" font-size="28" text-anchor="middle" textLength="162" lengthAdjust="spacingAndGlyphs">21 555 0148</text>
    <text class="dimension" x="587" y="505" text-anchor="middle">770 mm</text>
    <text class="dimension" transform="translate(726 610) rotate(-90)" text-anchor="middle">550 mm</text>
    <text class="dimension" transform="translate(726 718) rotate(-90)" text-anchor="middle">285 mm</text>
  </g>

  <!-- Front corner, right -->
  <g class="front-corner-right">
    <polygon class="panel-red" points="839,508 839,673 776,687"/>
    <polygon class="panel-yellow" points="776,687 839,673 839,759 775,759"/>
    <polygon class="side-frame" points="839,508 839,759 775,759 776,687"/>
  </g>

  <!-- Front panel, exterior cleaning -->
  <g class="front-right-panel">
    <rect class="panel-deep-red" x="939" y="506" width="201" height="10"/>
    <polygon class="panel-red" points="939,546 1140,546 1140,710 939,669"/>
    <rect class="panel-yellow" x="939" y="515" width="201" height="31"/>
    <polygon class="panel-yellow" points="939,669 1140,710 1140,757 939,766"/>
    <rect x="950" y="690" width="186" height="75" fill="url(#mud-fill)" role="img" aria-label="Mud splash spattered across the panel"/>
    <text class="stencil stencil-dark" x="953" y="528" font-size="14.5" textLength="157" lengthAdjust="spacingAndGlyphs">EXTERIOR PROPERTY</text>
    <text class="stencil stencil-dark" x="953" y="543" font-size="14.5" textLength="73" lengthAdjust="spacingAndGlyphs">CLEANING</text>
    <g class="sans service-list" font-size="6.6">
      <text x="951" y="559">• Water Blasting</text>
      <text x="951" y="571">• House Washing / Soft wash</text>
      <text x="951" y="583">• Spouting/ Gutter Clearing</text>
      <text x="951" y="595">• Deck Cleaning</text>
      <text x="951" y="607">• Moss and Mould Treatment</text>
      <text x="951" y="619">• Cleaning Driveways and Paths</text>
      <text x="951" y="631">• Sanitize Playground Equipment</text>
      <text x="951" y="643">• Sanitize Outdoor Seating</text>
      <text x="951" y="655">• Clean Solar Panels</text>
      <text x="951" y="667">• Fence Cleaning</text>
    </g>
    <text class="dimension" x="1050" y="502" text-anchor="middle">682 mm</text>
    <text class="dimension" transform="translate(937 639) rotate(-90)" text-anchor="middle">880 mm</text>
    <text class="dimension" transform="translate(1153 639) rotate(-90)" text-anchor="middle">850 mm</text>
  </g>
</svg>
</body>
</html>
```